Post Card Design Bright Lantern Youth

We need a postcard design that will be mailed to all residents offering free pickups of donated clothing. Our foundation is called Bright Lantern Youth, we are a nonprofit charitable organization that provides meals and medical services to children in need in Honduras. Collecting unwanted second-hand clothing generates revenue that helps fund the mission and programs run by our foundation. We would like to offer our pickup services to everyone who has any unwanted reusable clothing.

```html
<!DOCTYPE html>
<html lang="en">
<head>
<meta charset="utf-8">
<title>Bright Lantern Youth – Postcard</title>
<link rel="stylesheet" href="https://fonts.googleapis.com/css2?family=Poppins:wght@500;600;700&display=swap">
<style>
  :root{
    --blue:#1a8fd6;
    --magenta:#e0107f;
    --yellow:#f7c600;
    --green:#6cbb2c;
    --ink:#1d1d1d;
    --paper:#ffffff;
    --mist:#f1f2f4;
    --bg:#cfcfcf;
    --stamp:#d6d7d9;
  }
  *{box-sizing:border-box;margin:0;padding:0}
  html,body{width:1091px;height:1200px;overflow:hidden;background:var(--bg)}
  body{position:relative;font-family:"Poppins",sans-serif;color:var(--ink)}
  .card{position:absolute;left:115px;width:860px;height:573px;background:var(--paper);overflow:hidden;box-shadow:0 6px 18px rgba(0,0,0,.25)}
  .card--front{top:18px}
  .card--back{top:609px}
  .card svg.art{position:absolute;inset:0;width:860px;height:573px}
  .txt{position:absolute;white-space:nowrap}
  .brand-name{font-weight:700;color:var(--green);font-size:30px;line-height:1}
  .headline{left:63px;top:205px;font-weight:700;font-size:44px;line-height:46px}
  .headline .l1{color:var(--blue);display:block}
  .headline .l2{color:var(--magenta);display:block}
  .subhead{left:63px;top:310px;font-weight:600;font-size:22px;line-height:25px}
  .mission{left:0;width:860px;top:440px;text-align:center;font-size:11.5px;line-height:16px;font-weight:500;white-space:normal;padding:0 70px}
  .contact-bar{left:0;width:860px;top:520px;display:flex;justify-content:center;align-items:center;gap:10px;color:#fff;font-weight:600;font-size:19px}
  .contact-bar .sep{opacity:.9}
  .ico{display:inline-flex;align-items:center;gap:5px}
  .ico svg{width:17px;height:17px}
  .dot{display:inline-block;width:16px;height:16px;border-radius:50%;background:#fff;margin-left:4px}
  .pickup{left:52px;top:36px;color:#fff;font-weight:600;font-size:15px;line-height:18px}
  .support-pill{left:45px;top:336px;background:var(--green);color:#fff;font-weight:700;font-size:17px;padding:2px 16px;border-radius:14px}
  .support-body{left:45px;top:376px;font-size:11.8px;line-height:14.5px;font-weight:500}
  .phone-big{left:45px;top:485px;color:#fff;font-weight:700;font-size:32px;display:flex;align-items:center;gap:6px}
  .phone-big svg{width:26px;height:26px}
  .contact-small{left:45px;top:533px;color:#fff;font-weight:600;font-size:11.5px;display:flex;align-items:center;gap:6px}
  .contact-small .dot{width:11px;height:11px;margin-left:2px}
  .back-brand{left:560px;top:112px;width:140px;text-align:center;white-space:normal;font-size:21px;line-height:24px}
  .stamp{left:717px;top:30px;width:97px;height:98px;background:var(--stamp)}
</style>
</head>
<body>

<!-- FRONT -->
<section class="card card--front">
  <svg class="art" viewBox="0 0 860 573" aria-hidden="false">
    <defs>
      <linearGradient id="crowd" x1="0" y1="0" x2="1" y2="1">
        <stop offset="0" stop-color="#7d7b74"/><stop offset=".5" stop-color="#4a4640"/><stop offset="1" stop-color="#2f3a4a"/>
      </linearGradient>
      <linearGradient id="kids" x1="0" y1="0" x2="1" y2="1">
        <stop offset="0" stop-color="#a7b2b8"/><stop offset="1" stop-color="#3f5a78"/>
      </linearGradient>
    </defs>
    <ellipse cx="260" cy="200" rx="200" ry="150" fill="var(--mist)"/>
    <path d="M0 0H90C95 25 75 35 60 40C40 48 45 70 25 85C15 92 5 90 0 88Z" fill="var(--green)"/>
    <path d="M350 0C325 140 390 330 560 390C690 435 800 405 860 375V0Z" fill="var(--blue)"/>
    <path role="img" aria-label="Photo of volunteers preparing food for a community meal" d="M372 0C352 135 410 310 570 365C690 405 800 385 860 355V0Z" fill="url(#crowd)"/>
    <circle cx="503" cy="287" r="121" fill="var(--green)"/>
    <circle cx="503" cy="287" r="111" fill="#fff"/>
    <circle role="img" aria-label="Photo of children holding a large photo frame" cx="503" cy="287" r="104" fill="url(#kids)"/>
    <path d="M0 432C250 395 600 390 860 410V505H0Z" fill="var(--yellow)"/>
    <rect y="505" width="860" height="68" fill="var(--magenta)"/>
  </svg>

  <div class="txt brand-name" style="left:63px;top:160px">Bright Lantern Youth</div>
  <h1 class="txt headline"><span class="l1">Let’s Make</span><span class="l2">a Difference</span></h1>
  <p class="txt subhead">Bringing Sustainable<br>Supplies, Food, and Water<br>to Communities in Need</p>
  <p class="txt mission">For over 7 years, Bright Lantern Youth has been a non-profit offering feeding program worldwide. We feel that communities as a whole benefit when individuals are empowered to care for their most vulnerable population. Our team works hard to go to communities to eliminate hunger that others don’t reach.</p>
  <div class="txt contact-bar">
    <span class="ico"><svg viewBox="0 0 24 24"><circle cx="12" cy="12" r="12" fill="#fff"/><path d="M8 6l2 3-1.3 1.5c.8 1.8 2 3 3.8 3.8L14 13l3 2-1 2.5c-5 .3-9.8-4.5-9.5-9.5z" fill="var(--magenta)"/></svg>(555) 014-2278</span>
    <span class="sep">|</span>
    <span class="ico"><svg viewBox="0 0 24 24"><circle cx="12" cy="12" r="12" fill="#fff"/><rect x="6" y="8" width="12" height="8" fill="none" stroke="var(--magenta)" stroke-width="1.6"/><path d="M6 8l6 5 6-5" fill="none" stroke="var(--magenta)" stroke-width="1.6"/></svg>info@brightlanternyouth.org</span>
    <span class="sep">|</span>
    <span class="ico"><svg viewBox="0 0 24 24"><circle cx="12" cy="12" r="12" fill="#fff"/><circle cx="12" cy="12" r="6" fill="none" stroke="var(--magenta)" stroke-width="1.6"/><path d="M6 12h12M12 6v12" stroke="var(--magenta)" stroke-width="1.4"/></svg>brightlanternyouth.org</span>
    <span><span class="dot"></span><span class="dot"></span></span>
  </div>
</section>

<!-- BACK -->
<section class="card card--back">
  <svg class="art" viewBox="0 0 860 573">
    <defs>
      <linearGradient id="family" x1="0" y1="0" x2="1" y2="1">
        <stop offset="0" stop-color="#e9e3da"/><stop offset=".5" stop-color="#b79a86"/><stop offset="1" stop-color="#8d93a6"/>
      </linearGradient>
      <linearGradient id="van" x1="0" y1="0" x2="1" y2="1">
        <stop offset="0" stop-color="#3a3d44"/><stop offset="1" stop-color="#9fc3c9"/>
      </linearGradient>
      <linearGradient id="girl" x1="0" y1="0" x2="1" y2="1">
        <stop offset="0" stop-color="#c9b79a"/><stop offset="1" stop-color="#8f7a66"/>
      </linearGradient>
    </defs>
    <ellipse cx="620" cy="330" rx="210" ry="160" fill="var(--mist)"/>
    <path d="M405 0C455 120 470 260 420 573H440C495 260 475 120 425 0Z" fill="var(--yellow)"/>
    <path d="M0 0H405C420 40 425 85 420 120H0Z" fill="var(--blue)"/>
    <path role="img" aria-label="Photo of a family on a sofa sorting clothes into a donation box" d="M0 120H420C420 200 400 260 380 320C260 300 120 310 0 330Z" fill="url(#family)"/>
    <circle cx="422" cy="189" r="92" fill="var(--green)"/>
    <circle cx="422" cy="189" r="82" fill="#fff"/>
    <circle role="img" aria-label="Photo of bottled water cases loaded in a van" cx="422" cy="189" r="76" fill="url(#van)"/>
    <circle cx="463" cy="370" r="82" fill="var(--magenta)"/>
    <circle cx="463" cy="370" r="73" fill="#fff"/>
    <circle role="img" aria-label="Photo of a young girl with a school backpack" cx="463" cy="370" r="67" fill="url(#girl)"/>
    <path d="M0 478C120 450 300 460 400 520C440 545 460 560 480 573H0Z" fill="var(--magenta)"/>
  </svg>

  <p class="txt pickup">We offer a pick-up service to anyone who<br>has unwanted clothing and generate<br>income that helps fund the mission and<br>programs run by our foundation.</p>
  <div class="txt brand-name back-brand">Bright Lantern Youth</div>
  <div class="txt stamp"></div>
  <div class="txt support-pill">Share Your Support</div>
  <p class="txt support-body">We are actively partnering with contributors to<br>lift the burden of extreme poverty and support our<br>cause. Our compassionate team aims to counter<br>malnutrition and purchase bulk items to give<br>children the long-term nutrition they require.</p>
  <div class="txt phone-big"><svg viewBox="0 0 24 24"><circle cx="12" cy="12" r="12" fill="#fff"/><path d="M8 6l2 3-1.3 1.5c.8 1.8 2 3 3.8 3.8L14 13l3 2-1 2.5c-5 .3-9.8-4.5-9.5-9.5z" fill="var(--magenta)"/></svg>(555) 014-2278</div>
  <div class="txt contact-small"><span>info@brightlanternyouth.org</span><span>|</span><span>brightlanternyouth.org</span><span><span class="dot"></span><span class="dot"></span></span></div>
</section>

</body>
</html>
```